Tr construction holdings pty ltd

2 sided card black and red with white
Very professional and elegant

Target Market(s)

Construction and Development

Industry/Entity Type

Construction and development

Contact Information for Business Card

One side black, one side red/or white business logo in top corner, email: morgan@trbuildworks.example

Requirements
Should not have
• Blue

```html
<!DOCTYPE html>
<html lang="en">
<head>
<meta charset="utf-8">
<title>TR Construction – Business Card</title>
<link href="https://fonts.googleapis.com/css2?family=Quicksand:wght@500;700&display=swap" rel="stylesheet">
<style>
  :root {
    --card-black: #000000;
    --card-red: #e83a1f;
    --ink-white: #ffffff;
    --mark-tint: rgba(255, 255, 255, 0.16);
  }
  * { margin: 0; padding: 0; box-sizing: border-box; }
  html, body {
    width: 981px;
    height: 1200px;
    overflow: hidden;
    background: var(--card-black);
  }
  .canvas {
    width: 981px;
    height: 1200px;
    display: flex;
    flex-direction: column;
  }
  .card-side {
    position: relative;
    width: 981px;
    height: 600px;
    overflow: hidden;
    font-family: "Quicksand", sans-serif;
    color: var(--ink-white);
  }
  .card-side--black { background: var(--card-black); }
  .card-side--red { background: var(--card-red); }

  .brand {
    position: absolute;
    top: 68px;
    left: 592px;
    width: 312px;
    text-align: center;
    font-weight: 700;
    color: var(--ink-white);
    line-height: 1;
  }
  .brand__initials {
    display: block;
    font-size: 62px;
    letter-spacing: 2px;
  }
  .brand__name {
    display: block;
    margin-top: 8px;
    font-size: 31px;
    letter-spacing: 1px;
  }

  .backdrop-initials {
    position: absolute;
    left: -18px;
    top: 300px;
    font-family: "Quicksand", sans-serif;
    font-weight: 700;
    font-size: 400px;
    line-height: 1;
    letter-spacing: -6px;
    color: var(--mark-tint);
    user-select: none;
  }

  .contact-email {
    position: absolute;
    left: 544px;
    top: 543px;
    font-size: 26px;
    font-weight: 500;
    letter-spacing: 0.3px;
    color: var(--ink-white);
    white-space: nowrap;
  }
</style>
</head>
<body>
<main class="canvas">
  <section class="card-side card-side--black" aria-label="Card front">
    <div class="brand">
      <span class="brand__initials">TR</span>
      <span class="brand__name">CONSTRUCTION.</span>
    </div>
    <div class="backdrop-initials" aria-hidden="true">TR</div>
    <p class="contact-email">morgan@trbuildworks.example</p>
  </section>

  <section class="card-side card-side--red" aria-label="Card back">
    <div class="brand">
      <span class="brand__initials">TR</span>
      <span class="brand__name">CONSTRUCTION.</span>
    </div>
    <div class="backdrop-initials" aria-hidden="true">TR</div>
    <p class="contact-email">morgan@trbuildworks.example</p>
  </section>
</main>
</body>
</html>
```